A private psychotherapy practice for seniors located on the upper west side of manhattan needs a pos

**Hi, Please note deadline was decreased by two days**

I am a Psychotherapist (LCSW) who has a Private Practice located on the Upper West Side of Manhattan. I accept Vitalcare and most other insurances. I treat Seniors who have health or financial issues, loss of spouse, feel sad most days, withdraw from social activities or have problems sleeping or eating. Psychotherapy allows individuals to relieve their feelings of sadness and to enjoy life again. I am a licensed clinical social worker with over fifteen years of experience and advanced training from Calderwood Analytic Academy.

Target Market(s)

Senior Citizens (65+) living on the upper west side of manhattan

Font styles to use
Serif

Requirements
Must have
• Broad appeal - diversified ethnic group if photos are used. Clear call to help those struggling with aging issues - especially living in New York City
Nice to have
• Hopeful and improved quality of life as result of psychotherapy treatment. Improved relations with family and friends.
Should not have
• Not depressing or too psycho bable.

```html
<!DOCTYPE html>
<html lang="en">
<head>
<meta charset="utf-8">
<title>Senior Psychotherapy Postcard</title>
<link href="https://fonts.googleapis.com/css2?family=Open+Sans:wght@400;600;700;800&family=Roboto+Condensed:wght@400;700&display=swap" rel="stylesheet">
<style>
:root{
  --bg:#d9d9d9;
  --blue:#1f6fb0;
  --blue-dark:#0f3f73;
  --blue-mid:#2d86c8;
  --green:#7bc142;
  --green-dark:#4e9a26;
  --black:#111;
  --white:#fff;
  --text:#fdfdfd;
}
*{margin:0;padding:0;box-sizing:border-box}
html,body{width:791px;height:1200px;overflow:hidden;background:var(--bg);font-family:"Open Sans",sans-serif}
.postcard{position:absolute;left:32px;width:733px;height:567px;background:var(--white);box-shadow:0 4px 14px rgba(0,0,0,.35);overflow:hidden}
.front{top:13px}
.back{top:607px}
.photo-group{position:absolute;left:0;top:0;width:733px;height:330px;background:linear-gradient(180deg,#8fb3c4 0%,#c9b59a 55%,#e9e3dc 100%)}
.front-shapes{position:absolute;left:0;top:0}
.badge{position:absolute;left:18px;top:162px;width:150px;height:150px}
.badge-text{position:absolute;left:18px;top:190px;width:150px;text-align:center;font-family:"Roboto Condensed",sans-serif;font-weight:700;color:var(--black);line-height:1.05}
.badge-text .big{font-size:26px}
.badge-text .mid{font-size:20px;color:var(--white)}
.badge-text .small{font-size:17px}
.headline{position:absolute;left:28px;top:322px;width:340px;font-family:"Roboto Condensed",sans-serif;font-weight:700;color:var(--white);text-transform:uppercase}
.headline .l1{font-size:24px;letter-spacing:.2px}
.headline .l2{font-size:28px;color:var(--green);font-weight:400;margin-top:2px}
.headline .l3{font-size:13.5px;font-weight:400;margin-top:6px}
.contacts{position:absolute;font-size:16px;color:var(--white);line-height:1.55}
.contacts li{list-style:none;display:flex;align-items:center;gap:8px}
.contacts svg{flex:none}
.front .contacts{left:40px;top:470px}
.credentials{position:absolute;left:400px;top:372px;width:300px;height:112px;background:var(--black);padding:10px 14px;color:var(--white);font-size:17px;line-height:1.3}
.credentials em{font-style:normal;color:var(--green)}
.follow{position:absolute;right:36px;bottom:30px;display:flex;align-items:center;gap:10px;color:var(--white);font-size:17px;font-weight:600}
.follow span.dot{width:22px;height:22px;border-radius:50%;background:var(--green)}
.back-shapes{position:absolute;left:0;top:0}
.about{position:absolute;left:40px;top:40px;width:300px;color:var(--text);font-size:17px;line-height:1.42;text-align:justify}
.care-image{position:absolute;left:158px;top:290px;width:150px;height:150px;border-radius:50%;border:6px solid var(--white);background:radial-gradient(circle at 40% 40%,#dfeef7,#6da6cf 70%,#2b5f8d);box-shadow:0 0 0 3px var(--green)}
.back .contacts{left:40px;top:470px}
.stamp{position:absolute;right:40px;top:30px;width:80px;height:92px;border:1.5px solid #999}
</style>
</head>
<body>

<section class="postcard front">
  <div class="photo-group" role="img" aria-label="Photo of a diverse group of smiling friends standing together outdoors"></div>
  <svg class="front-shapes" width="733" height="567" viewBox="0 0 733 567">
    <path d="M0 290 C180 250 420 300 733 235 L733 567 L0 567Z" fill="var(--green)"/>
    <path d="M0 300 C200 262 430 312 733 250 L733 567 L0 567Z" fill="var(--blue)"/>
    <path d="M0 300 L380 300 C395 350 392 420 380 455 L0 455Z" fill="var(--blue-mid)" opacity=".55"/>
    <path d="M0 455 C150 440 300 460 400 450 L400 567 L0 567Z" fill="var(--blue-dark)"/>
    <path d="M0 520 C200 480 480 520 733 470 L733 567 L0 567Z" fill="var(--black)" opacity=".85"/>
    <path d="M0 528 C220 490 480 528 733 480" stroke="var(--green)" stroke-width="5" fill="none"/>
  </svg>
  <svg class="badge" viewBox="0 0 100 100" aria-hidden="true">
    <polygon fill="var(--green)" stroke="var(--green-dark)" stroke-width="1.5" points="50,2 57,12 69,6 72,18 85,17 83,30 95,35 88,46 98,55 87,63 92,75 79,78 78,91 66,88 59,98 50,90 41,98 34,88 22,91 21,78 8,75 13,63 2,55 12,46 5,35 17,30 15,17 28,18 31,6 43,12"/>
  </svg>
  <div class="badge-text">
    <div class="big">Accept</div>
    <div class="mid">Vitalcare</div>
    <div class="small">and other<br>Insurance</div>
  </div>
  <div class="headline">
    <div class="l1">A Private Psychotherapy Practice</div>
    <div class="l2">For Seniors Located</div>
    <div class="l3">On the Upper West Side of Manhattan</div>
  </div>
  <ul class="contacts">
    <li><svg width="14" height="14" viewBox="0 0 24 24"><path fill="#fff" d="M6.6 10.8a15 15 0 006.6 6.6l2.2-2.2c.3-.3.7-.4 1-.2 1.1.4 2.3.6 3.6.6.6 0 1 .4 1 1V20c0 .6-.4 1-1 1A17 17 0 013 4c0-.6.4-1 1-1h3.5c.6 0 1 .4 1 1 0 1.3.2 2.5.6 3.6.1.3 0 .7-.2 1z"/></svg>123-456-789</li>
    <li><svg width="12" height="12"><circle cx="6" cy="6" r="6" fill="var(--green)"/></svg>info@westsidecounsel.com</li>
    <li><svg width="12" height="12"><circle cx="6" cy="6" r="6" fill="var(--green)"/></svg>westsidecounsel.com</li>
  </ul>
  <div class="credentials">Licensed clinical social worker with over <em>15 years of experience</em> and <em>advanced training</em> from Calderwood Analytic Academy</div>
  <div class="follow">Follow us <span class="dot"></span><span class="dot"></span></div>
</section>

<section class="postcard back">
  <svg class="back-shapes" width="733" height="567" viewBox="0 0 733 567">
    <path d="M0 0 L330 0 C370 120 390 330 345 567 L0 567Z" fill="var(--green)"/>
    <path d="M0 0 L318 0 C356 120 374 330 332 567 L0 567Z" fill="var(--blue)"/>
    <path d="M0 0 L250 0 C290 160 300 330 280 567 L0 567Z" fill="var(--blue-dark)" opacity=".35"/>
    <path d="M0 460 L300 460 C310 490 305 520 300 550 L0 550Z" fill="var(--black)"/>
  </svg>
  <p class="about">I am a Psychotherapist (LCSW) who has a Private Practice located on the Upper West Side of Manhattan I treat Seniors who have health or financial issues, loss of spouse, feel sad most days, withdraw from social activities or have problems sleeping or eating. Psychotherapy allows individuals to relieve their feelings of sadness and to enjoy life again.</p>
  <div class="care-image" role="img" aria-label="Close-up photo of a stethoscope resting on a keyboard"></div>
  <ul class="contacts">
    <li><svg width="14" height="14" viewBox="0 0 24 24"><path fill="#fff" d="M6.6 10.8a15 15 0 006.6 6.6l2.2-2.2c.3-.3.7-.4 1-.2 1.1.4 2.3.6 3.6.6.6 0 1 .4 1 1V20c0 .6-.4 1-1 1A17 17 0 013 4c0-.6.4-1 1-1h3.5c.6 0 1 .4 1 1 0 1.3.2 2.5.6 3.6.1.3 0 .7-.2 1z"/></svg>123-456-789</li>
    <li><svg width="12" height="12"><circle cx="6" cy="6" r="6" fill="var(--green)"/></svg>info@westsidecounsel.com</li>
    <li><svg width="12" height="12"><circle cx="6" cy="6" r="6" fill="var(--green)"/></svg>westsidecounsel.com</li>
  </ul>
  <div class="stamp"></div>
</section>

</body>
</html>
```